Australian Craft Distillery needs poster layout for its awesome Manifesto

Tall Finch's a small craft distillery based in the Brook Flats of Western Australia producing award-winning vodkas and gin. Check out our website www.tallfinchs-example.com.au to get a feel for our design aesthetic, especially from our bottle design. We are "Small Batch Liquors - Out of the Brook Flats". Everything we do reflects that.
We have a manifesto - The Tall Finch's Manifesto -that we proudly display in our tasting room, and was used as a basis for an artwork in our entry.
We've had a number of customers ask to buy a poster of the manifesto (attached) so I want to commission a more professional design than the current layout which was put together in Word! (yes I know, I'm sorry, I did move it into Illustrator later).
I think the text flows in a sequential order so I'm looking for a design that you read from start to finish rather than a random collection of statements. I'd like to include our logo in the design somewhere but it doesn't have to be front and centre. There is a secondary logo device as well - the interlocked T and F on the label which could be used. I'm assuming the print will be simple black on either a plain background or a "craft background" similar to the labels. Our current fonts are SchmutzICG for text and VeneerTwo for headings. The label uses Haymaker and Gin-Rough.
Print size will be A3 (prefer the design to be to this proportion and portrait orientation) and bigger up to A1. We'll print the final design on the back of t-shirts for staff as well. If I was going to sum up our style in a couple of words it would be "intelligently irreverent" Have fun with this, I certainly did writing it!

```html
<!DOCTYPE html>
<html lang="en">
<head>
<meta charset="utf-8">
<title>The Tall Finch's Manifesto</title>
<link rel="stylesheet" href="https://fonts.googleapis.com/css2?family=Oswald:wght@500;700&family=Comfortaa:wght@400&display=swap">
<style>
  :root {
    --ink: #000000;
    --backdrop-deep: #070707;
    --backdrop-warm: #1b1814;
    --paper: #ffffff;
    --signal-red: #e4121b;
  }
  * { box-sizing: border-box; margin: 0; padding: 0; }
  html, body { width: 901px; height: 1200px; overflow: hidden; background: var(--ink); }
  .poster {
    position: relative;
    width: 901px;
    height: 1200px;
    overflow: hidden;
    background: var(--ink);
    color: var(--paper);
  }
  .label-collage {
    position: absolute;
    inset: 0;
    background:
      radial-gradient(ellipse at 30% 25%, var(--backdrop-warm) 0%, transparent 55%),
      radial-gradient(ellipse at 80% 60%, var(--backdrop-warm) 0%, transparent 50%),
      radial-gradient(ellipse at 20% 80%, #141210 0%, transparent 50%),
      var(--backdrop-deep);
  }
  .brand-mark {
    position: absolute;
    left: 0; right: 0;
    top: 100px;
    display: flex;
    justify-content: center;
    align-items: center;
    gap: 10px;
    font-family: "Oswald", sans-serif;
    font-weight: 700;
    font-size: 34px;
    letter-spacing: 1px;
    text-transform: uppercase;
    color: var(--paper);
  }
  .brand-mark .brand-square {
    width: 16px; height: 16px;
    background: var(--paper);
  }
  .bottle-cap {
    position: absolute;
    left: 392px; top: 237px;
    width: 110px; height: 56px;
  }
  .bottle-base {
    position: absolute;
    left: 335px; top: 1127px;
    width: 226px; height: 40px;
  }
  .manifesto-title {
    position: absolute;
    left: 0; right: 0;
    top: 298px;
    text-align: center;
    font-family: "Oswald", sans-serif;
    font-weight: 700;
    color: var(--signal-red);
    text-transform: uppercase;
    line-height: 0.98;
  }
  .manifesto-title .title-line { display: block; font-size: 31px; letter-spacing: -0.5px; }
  .manifesto-title .title-line--small { font-size: 21px; }
  .manifesto-subtitle {
    position: absolute;
    left: 325px; top: 382px;
    width: 250px;
    text-align: center;
    font-family: "Oswald", sans-serif;
    font-weight: 500;
    font-size: 21px;
    line-height: 1.1;
    letter-spacing: -0.6px;
    text-transform: uppercase;
    transform: rotate(5deg);
  }
  .manifesto-body {
    position: absolute;
    left: 320px; top: 438px;
    width: 260px;
    text-align: center;
    font-family: "Comfortaa", sans-serif;
    font-size: 11px;
    line-height: 14px;
    white-space: nowrap;
  }
  .manifesto-body .section-cue { margin: 1px 0 2px; }
  .manifesto-body .section-cue--spaced { margin-top: 14px; }
  .manifesto-body .tenet { margin-bottom: 2px; }
  .manifesto-body .tenet--tilt-up { transform: rotate(-3deg); }
  .manifesto-body .tenet--tilt-down { transform: rotate(3deg); }
</style>
</head>
<body>
<main class="poster">
  <div class="label-collage" role="img" aria-label="Faint dark collage of vintage spirit labels and stamps"></div>

  <div class="brand-mark"><span class="brand-square"></span>Tall Finch's</div>

  <svg class="bottle-cap" viewBox="0 0 110 56" aria-hidden="true">
    <path d="M4 8 Q4 2 12 2 H98 Q106 2 106 8 V44 H4 Z" fill="#ffffff"/>
    <ellipse cx="55" cy="48" rx="53" ry="6" fill="#ffffff"/>
    <ellipse cx="55" cy="44" rx="53" ry="4" fill="#000000"/>
    <path d="M2 44 Q55 56 108 44" fill="none" stroke="#ffffff" stroke-width="2"/>
  </svg>

  <h1 class="manifesto-title">
    <span class="title-line">The Tall</span>
    <span class="title-line">Finch's</span>
    <span class="title-line title-line--small">Manifesto</span>
  </h1>

  <p class="manifesto-subtitle">(Our thoughts on life,<br>a.k.a. how to be better)</p>

  <section class="manifesto-body">
    <p class="section-cue">first</p>
    <p class="tenet tenet--tilt-down">• Work Smart • Love Hard • Play Often<br>• Sleep More •</p>
    <p class="tenet tenet--tilt-down">• Stay Present • Be Local • Embrace<br>Silly • Get Dirty (but) Stay Clean •<br>• Laugh • Cry • Run • Dance • Sing •<br>• Stop That (and) Slow down •</p>

    <p class="section-cue section-cue--spaced">then</p>
    <p class="tenet tenet--tilt-up">• Celebrate others success • Don't be<br>shit •</p>
    <p class="tenet tenet--tilt-down">• Have one thing you are awesome at<br>•</p>
    <p class="tenet tenet--tilt-down">• Get off your phone • Show some<br>fucking passion •</p>
    <p class="tenet tenet--tilt-down">• Make something • Making money<br>doesn't count • Making babies does •</p>
    <p class="tenet tenet--tilt-down">• Never stop exploring, never stop<br>learning, share that with others •</p>
    <p class="tenet tenet--tilt-down">• We all fuck up. Make good, learn, be<br>better and move on •</p>
    <p class="tenet tenet--tilt-down">• Life is far too short, squeeze every<br>drop out of it •</p>
    <p class="section-cue">and, of course</p>
    <p class="tenet">• Drink better •</p>

    <p class="section-cue section-cue--spaced">and finally</p>
    <p class="tenet tenet--tilt-down">• Sometimes you just won't under-<br>stand •</p>
    <p class="tenet">• An argument is not a fight •</p>
    <p class="tenet tenet--tilt-down">• You are not as important as you<br>think •</p>
    <p class="tenet tenet--tilt-down">• You are more loved than you think •</p>
    <p class="tenet">• Its ok to do things alone •</p>
    <p class="tenet">• Its ok not to be busy •</p>
    <p class="tenet tenet--tilt-down">• There is no good reason to do a half<br>arsed job •</p>
    <p class="tenet tenet--tilt-down">• Teaching is the best way of learning •</p>
    <p class="tenet tenet--tilt-down">• The past is important, what you do<br>next is much more so •</p>
    <p class="tenet tenet--tilt-down">• Change is inevitable, roll with it •</p>
    <p class="tenet tenet--tilt-down">• Success is whatever you decide it to<br>be •</p>
  </section>

  <svg class="bottle-base" viewBox="0 0 226 40" aria-hidden="true">
    <ellipse cx="113" cy="20" rx="112" ry="19" fill="#ffffff"/>
  </svg>
</main>
</body>
</html>
```